qLM Builders
Nimble Site Crafting
draft #229 - This looks pretty good. We prefer option 2 for the stationary. Clean and simple. We aren't so sure about the colored watermark. Seems like too much maybe
draft #223 - We really like the back of this one!
The contests has been extended for 3 more days. Please submit new designs. Due to the short time frame, we will only be accepting and rating full designs including complete stationary.
I will make every effort to provide feedback as soon as possible on designs concepts. Thank!
draft #96 - I like the back! The front is a little cookie cutter. Can you try something that integrates the "X" into the design. I don't really like the text all centered (draft #95,draft #94)
draft #102 I don't like the graphic at the top, but I like the back and I like how you integrated the X on the front like a watermark. can you remove that and add some icon's for phone,email, ect?
Some design inspiration - here are some cards we like
http://www.cardmarket.example/theme_previews/1778907-stylish-business-card?index=4
http://cardmarket.example/item/royal-modern-business-card/2484567?WT.ac=category_thumb&WT.seg_1=category_thumb&WT.z_author=omar-lindqvest
http://cardmarket.example/item/awesomeness-business-card/55256?WT.ac=category_thumb&WT.seg_1=category_thumb&WT.z_author=Bram
http://cardmarket.example/item/qr-business-card/1361513?WT.ac=category_thumb&WT.seg_1=category_thumb&WT.z_author=Marisk
http://cardmarket.example/item/clean-modern-business-card/1922436?WT.ac=category_thumb&WT.seg_1=category_thumb&WT.z_author=dustwick
http://cardmarket.example/theme_previews/1492534-neat-corporate-business-card?index=9
http://cardmarket.example/item/red-business-card/504464?WT.ac=category_thumb&WT.seg_1=category_thumb&WT.z_author=lumenpress
Also meant to mention, we prefer square cards (instead of the rounded corners).
If you have ideas for texture/embossing that would look nice please include! We are digging the glossy look on the back of some of these. But any details that help make the card unique is great!
thanks again!
Hi Designers. We got backed up and haven't been able to provide feedback yet.
There are also A LOT of designs to go through. We will be eliminating design's I consider "cookie cutter" templates. We are interested in unique designs that integrate the with the look and feel of the logo, or directly integrate parts of the logo with the designs.
In General, the Wavy/curvy look isn't what we are going for (there are A LOT of those).
There are some very unique integrations with the "X" that we like, especially when it's used kinda like a watermark.
We don't want any contact info on the back other then maybe the website.
Again thanks for your work! We will be sending specific feedback for the designs we like via PM in the next few hours.
Gavin@qlmbuilders
Thanks for all the designs and the note. We will be going through and selecting the few our favorite designs so far and offering tomorrow.
Thanks for the good work!
@PH - we will develop stationery for the liked business cards. Please let me know via private message. Thanks
sir please check pvt message top right side please
Note to Designers - This a a business Card & Stationary project. Designs should include concepts for both. Any questions or concerns please message me.

```html
<!DOCTYPE html>
<html lang="en">
<head>
<meta charset="utf-8">
<title>qLM Builders – Business Card</title>
<link rel="stylesheet" href="https://fonts.googleapis.com/css2?family=Titillium+Web:wght@400;600&display=swap">
<style>
  :root {
    --backdrop: #ecebe8;
    --card: #ffffff;
    --brand-blue: #29a8e0;
    --ink: #3a3a3a;
    --ink-soft: #5b5b5b;
    --on-blue: #ffffff;
  }
  * { box-sizing: border-box; margin: 0; padding: 0; }
  html, body {
    width: 1200px; height: 408px; overflow: hidden;
    background: var(--backdrop);
    font-family: "Titillium Web", Arial, sans-serif;
  }
  .sheet { position: relative; width: 1200px; height: 408px; }
  .card {
    position: absolute; top: 36px;
    width: 560px; height: 336px;
    background: var(--card);
    box-shadow: 0 2px 8px rgba(0,0,0,0.18);
    overflow: hidden;
  }
  .card--front { left: 32px; }
  .card--back { left: 608px; }

  .brand { position: absolute; left: 70px; top: 66px; }
  .brand__row { display: flex; align-items: center; gap: 12px; }
  .brand__mark { width: 28px; height: 28px; background: var(--brand-blue); }
  .brand__name {
    font-size: 40px; font-weight: 600; line-height: 1;
    color: var(--brand-blue); letter-spacing: 0.5px;
  }
  .brand__tagline {
    margin: 6px 0 0 40px;
    font-size: 17px; color: var(--ink); letter-spacing: 0.4px;
  }

  .band {
    position: absolute; left: 0; right: 0; top: 196px; height: 114px;
    background: var(--brand-blue);
  }
  .person { position: absolute; left: 18px; bottom: 14px; color: var(--on-blue); }
  .person__name { font-size: 17px; font-weight: 600; line-height: 1.2; }
  .person__role { font-size: 12px; line-height: 1.3; }

  .contact {
    position: absolute; left: 290px; top: 14px;
    color: var(--on-blue); font-size: 12px; line-height: 1.45;
  }
  .contact__address { margin-bottom: 16px; }
  .contact__label { display: inline-block; width: 22px; }

  .card--back .brand { left: 70px; top: 78px; }
  .back__line {
    position: absolute; left: 0; right: 0; top: 226px;
    text-align: center; font-size: 15px; font-weight: 600; color: var(--ink-soft);
  }
</style>
</head>
<body>
<main class="sheet">
  <section class="card card--front" aria-label="Business card front">
    <div class="brand">
      <div class="brand__row">
        <span class="brand__mark" aria-hidden="true"></span>
        <span class="brand__name">qLM Builders</span>
      </div>
      <p class="brand__tagline">Nimble Site Crafting</p>
    </div>
    <div class="band">
      <div class="person">
        <p class="person__name">Gavin Holloway</p>
        <p class="person__role">Owner, CEO</p>
      </div>
      <div class="contact">
        <p class="contact__address">218 Larkspur Lane, Dayton, OH 45402</p>
        <p><span class="contact__label">P :</span>5550142287</p>
        <p><span class="contact__label">E :</span>gavin@qlmbuilders.com</p>
        <p><span class="contact__label">W :</span>www.qlmbuilders.com</p>
      </div>
    </div>
  </section>

  <section class="card card--back" aria-label="Business card back">
    <div class="brand">
      <div class="brand__row">
        <span class="brand__mark" aria-hidden="true"></span>
        <span class="brand__name">qLM Builders</span>
      </div>
      <p class="brand__tagline">Nimble Site Crafting</p>
    </div>
    <p class="back__line">Builders + Nimble Site Crafting</p>
  </section>
</main>
</body>
</html>
```